Harborline Energy - needs a business card

Harborline Energy is a U.S. based diesel sourcing and distribution company that supports American oil & gas fields through providing quality product and consistent services.

Target Market(s)

Oil and Gas

Contact Information for Business Card

The background of the card must be white to ensure the logo pops.

Font styles to use
Serif
Sans Serif

Colors

Designer to choose colors to be used in the design.

Requirements
Must have
• Front of Card: Tag line: Harborline Energy, Powering America's Oil & Gas fields.
• Not sure if you guys do this part but just in case...
• Dale Menschow
• Owner/CEO
• C:555.318.4076
• E:Dmenschow@harborlineenergy.example
• W:Harborlineenergy.example
• Locations: Servicing the Powder River, DJ basin and Bakken formations.
• Back of Card: " Frac fueling is what we do. We understand how important diesel fuel is to your operation, which is why our main service line is Frac fueling. We assure our supply and stand by our service"

```html
<!DOCTYPE html>
<html lang="en">
<head>
<meta charset="utf-8">
<title>Harborline Energy – Business Card</title>
<link href="https://fonts.googleapis.com/css2?family=Fira+Sans:wght@300;400;600&display=swap" rel="stylesheet">
<style>
  :root {
    --navy: #1f2e5c;
    --red: #b01f26;
    --white: #ffffff;
    --stage: #e6e7ea;
    --card-w: 540px;
    --card-h: 309px;
  }
  * { box-sizing: border-box; margin: 0; padding: 0; }
  html, body { width: 1200px; height: 780px; overflow: hidden; }
  body {
    background: var(--stage);
    font-family: "Fira Sans", Arial, sans-serif;
    display: flex;
    align-items: center;
    justify-content: center;
    gap: 40px;
  }
  .card {
    position: relative;
    width: var(--card-w);
    height: var(--card-h);
    background: var(--white);
    overflow: hidden;
    box-shadow: 0 6px 18px rgba(0,0,0,.18);
  }
  .card-shapes { position: absolute; inset: 0; width: 100%; height: 100%; }

  /* Back side */
  .quote {
    position: absolute;
    top: 34px;
    right: 30px;
    width: 250px;
    color: var(--white);
    font-size: 11.5px;
    font-weight: 300;
    line-height: 1.55;
    text-align: right;
  }
  .brand {
    position: absolute;
    display: flex;
    align-items: center;
    gap: 10px;
    color: var(--navy);
    font-weight: 600;
    letter-spacing: .5px;
  }
  .brand-dot { border-radius: 50%; background: var(--red); flex: none; }
  .back .brand { left: 34px; top: 178px; font-size: 24px; }
  .back .brand-dot { width: 34px; height: 34px; }

  /* Front side */
  .front .brand { left: 24px; bottom: 62px; font-size: 21px; }
  .front .brand-dot { width: 28px; height: 28px; }
  .tagline {
    position: absolute;
    left: 24px;
    bottom: 38px;
    width: 250px;
    color: var(--navy);
    font-size: 9.5px;
    font-weight: 400;
    line-height: 1.3;
  }
  .identity {
    position: absolute;
    top: 36px;
    right: 30px;
    text-align: right;
    color: var(--white);
  }
  .identity .name { font-size: 29px; font-weight: 300; letter-spacing: .3px; }
  .identity .title { font-size: 12px; font-weight: 300; margin-top: 2px; }
  .contact {
    position: absolute;
    left: 300px;
    top: 128px;
    list-style: none;
    color: var(--white);
    font-size: 11px;
    font-weight: 300;
    line-height: 1.35;
  }
  .contact li { display: flex; gap: 8px; margin-bottom: 6px; }
  .contact svg { width: 10px; height: 10px; flex: none; margin-top: 2px; fill: var(--white); }
</style>
</head>
<body>

  <section class="card back" aria-label="Card back">
    <svg class="card-shapes" viewBox="0 0 540 309" preserveAspectRatio="none" aria-hidden="true">
      <rect width="540" height="309" fill="var(--red)"/>
      <path d="M0 96 H175 C250 96 305 150 305 212 C305 262 340 292 420 309 H0 Z" fill="var(--white)"/>
    </svg>
    <p class="quote">"Frac fueling is what we do. We understand how important diesel fuel is to your operation, which is why our main service line is Frac fueling. We assure our supply and stand by our service"</p>
    <div class="brand"><span class="brand-dot"></span>Harborline Energy</div>
  </section>

  <section class="card front" aria-label="Card front">
    <svg class="card-shapes" viewBox="0 0 540 309" preserveAspectRatio="none" aria-hidden="true">
      <path d="M150 0 H540 V309 H362 C335 185 255 118 150 0 Z" fill="var(--navy)"/>
      <path d="M134 0 H150 C255 118 335 185 362 309 H344 C318 200 240 130 134 0 Z" fill="var(--red)"/>
    </svg>
    <div class="identity">
      <p class="name">Dale Menschow</p>
      <p class="title">Owner/CEO</p>
    </div>
    <ul class="contact">
      <li><svg viewBox="0 0 10 10"><path d="M2 0 L4 2.5 L3 3.8 C3.8 5.3 4.7 6.2 6.2 7 L7.5 6 L10 8 L8.5 10 C4 9.5 .5 6 0 1.5 Z"/></svg>555.318.4076</li>
      <li><svg viewBox="0 0 10 10"><path d="M0 1.5 H10 V8.5 H0 Z M0.8 2.3 L5 5.4 L9.2 2.3 V2 H0.8 Z" fill-rule="evenodd"/></svg>Dmenschow@harborlineenergy.example</li>
      <li><svg viewBox="0 0 10 10"><circle cx="5" cy="5" r="4.3" fill="none" stroke="#fff" stroke-width="1"/><path d="M0.7 5 H9.3 M5 0.7 C2.5 3 2.5 7 5 9.3 M5 0.7 C7.5 3 7.5 7 5 9.3" fill="none" stroke="#fff" stroke-width=".8"/></svg>Harborlineenergy.example</li>
      <li><svg viewBox="0 0 10 10"><path d="M5 0 C2.6 0 1 1.7 1 3.8 C1 6.5 5 10 5 10 C5 10 9 6.5 9 3.8 C9 1.7 7.4 0 5 0 Z M5 2.4 A1.4 1.4 0 1 0 5 5.2 A1.4 1.4 0 1 0 5 2.4 Z" fill-rule="evenodd"/></svg>Servicing the Powder River,<br>DJ basin and Bakken formations.</li>
    </ul>
    <div class="brand"><span class="brand-dot"></span>Harborline Energy</div>
    <p class="tagline">Harborline Energy, Powering America's Oil &amp; Gas fields.</p>
  </section>

</body>
</html>
```